Digital Album Cover - Drifting Past Amber Harbor Lights (Piano & Cello)

HiI would like a digital album coverTitle: "Drifting Past Amber Harbor Lights (Piano & Cello)"Artist: "Rolf Dekker & The Osei Marit"

Requirements
Nice to have
• Original creativity
Should not have
• Copyrighted images

```html
<!DOCTYPE html>
<html lang="en">
<head>
<meta charset="utf-8">
<title>Drifting Past Amber Harbor Lights — Album Cover</title>
<link rel="stylesheet" href="https://fonts.googleapis.com/css2?family=Josefin+Sans:wght@400;600&display=swap">
<style>
  :root {
    --navy-deep: #16183f;
    --navy: #22256a;
    --violet: #3b40b4;
    --nebula-pink: #d9a3bd;
    --nebula-blue: #8088e2;
    --white: #ffffff;
    --ink: #1d1f4d;
    --line: rgba(255, 255, 255, 0.4);
  }
  html, body {
    margin: 0;
    padding: 0;
    width: 1200px;
    height: 1200px;
    overflow: hidden;
  }
  .album-cover {
    position: relative;
    width: 1200px;
    height: 1200px;
    background:
      radial-gradient(circle at 51% 50%, rgba(59, 64, 180, 0.45) 0%, transparent 45%),
      linear-gradient(180deg, var(--navy-deep) 0%, var(--navy) 55%, var(--navy-deep) 100%);
    font-family: "Josefin Sans", sans-serif;
    color: var(--white);
  }
  .cover-frame {
    position: absolute;
    inset: 29px;
    border: 2px solid rgba(255, 255, 255, 0.85);
  }
  .cover-geometry {
    position: absolute;
    inset: 0;
    width: 1200px;
    height: 1200px;
  }
  .cover-title {
    position: absolute;
    left: 0;
    right: 0;
    top: 1072px;
    margin: 0;
    text-align: center;
    font-weight: 600;
    font-size: 31px;
    line-height: 36px;
    letter-spacing: 0.22em;
    text-transform: uppercase;
  }
  .cover-artist {
    position: absolute;
    left: 349px;
    top: 1118px;
    width: 527px;
    height: 42px;
    margin: 0;
    background: var(--white);
    color: var(--ink);
    display: flex;
    align-items: center;
    justify-content: center;
    font-size: 15px;
    letter-spacing: 0.3em;
    text-transform: uppercase;
  }
</style>
</head>
<body>
  <main class="album-cover">
    <div class="cover-frame"></div>
    <svg class="cover-geometry" viewBox="0 0 1200 1200" xmlns="http://www.w3.org/2000/svg">
      <defs>
        <radialGradient id="artwork-fill" cx="50%" cy="50%" r="50%">
          <stop offset="0" stop-color="#ffffff"/>
          <stop offset="0.06" stop-color="#b9bdf2"/>
          <stop offset="0.35" stop-color="#7a74c9"/>
          <stop offset="0.6" stop-color="#4a4fb8"/>
          <stop offset="1" stop-color="#2b2f86"/>
        </radialGradient>
      </defs>
      <g class="guide-lines" fill="none" stroke="var(--line)" stroke-width="1.5">
        <circle cx="613" cy="605" r="392"/>
        <circle cx="613" cy="605" r="330"/>
        <line x1="613" y1="160" x2="613" y2="1050"/>
        <line x1="168" y1="605" x2="1058" y2="605"/>
        <line x1="298" y1="290" x2="928" y2="920"/>
        <line x1="928" y1="290" x2="298" y2="920"/>
      </g>
      <circle class="cover-artwork" cx="613" cy="605" r="290" fill="url(#artwork-fill)"
              role="img" aria-label="Star-shaped mandala of piano keys and geometric line work around a glowing nebula on a starry night sky"/>
    </svg>
    <h1 class="cover-title">Drifting Past Amber Harbor Lights</h1>
    <p class="cover-artist">Rolf Dekker &amp; The Osei Marit</p>
  </main>
</body>
</html>
```